eCommerce website for a DIY shop & communal center

We need a website for a business called The Makerloft Barn. The Makerloft Barn is both a shop and communal establishment where people with shared interests, especially in DIY (Do It Yourself) and crafting, can gather to shop for & work on projects while sharing ideas, equipment, supplies and knowledge. The shop is both brick & motor and online. The physical communal space provides workstations, equipment, tools and supplies and expertise for DIY lovers to create their projects.

Target Market(s)

Middle & upper class DIY enthusiasts, creative hobbyists, budding artists & small business owners

Industry/Entity Type

DIY, Arts & Crafts

Coding

Coded - Design and coding required

Number of Pages Required

5+ page

Requirements
Must have
• Menus to include 1. home page (with about us, operating hours, contacts, location, meet the team); 2. Studio activities (how to DIY at the Studio, booking, equipment & tools, house rules); 3. Studio events (events in the Studio, offsite events); 4. Resources (FAQs, tutorials, blogs, eBooks) and 5. Online shop
Nice to have
• Branding guidelines eg logo colours (see attachment) to influence design. Woo commerce shop. Booking feature for activities & events at the Studio.

```html
<!DOCTYPE html>
<html lang="en">
<head>
<meta charset="utf-8">
<title>The Makerloft Barn</title>
<link href="https://fonts.googleapis.com/css2?family=Montserrat:wght@400;500;600;700&family=Playball&display=swap" rel="stylesheet">
<style>
:root{
  --red:#c0202f;
  --dark:#1f1f1f;
  --ink:#222;
  --muted:#666;
  --light:#f4f4f4;
  --white:#fff;
  --field:#f2f2f2;
}
*{box-sizing:border-box;margin:0;padding:0}
html,body{width:1200px;height:3954px;overflow:hidden}
body{font-family:'Montserrat',sans-serif;color:var(--ink);background:var(--white);position:relative}
.abs{position:absolute}
.script{font-family:'Playball',cursive;font-weight:400}
.script .accent{color:var(--red)}
.btn{position:absolute;background:var(--red);color:var(--white);font-weight:700;font-size:15px;text-transform:uppercase;border-radius:6px;display:flex;align-items:center;justify-content:center;gap:10px}

/* header */
.site-header{position:absolute;left:0;top:0;width:1200px;height:111px;background:var(--dark)}
.brand-panel{position:absolute;left:0;top:0;width:439px;height:111px;background:var(--white);display:flex;align-items:center;padding-left:108px}
.brand-name{font-weight:700;font-size:30px;color:var(--dark);letter-spacing:-.5px}
.top-contact{position:absolute;right:111px;top:26px;color:var(--white);font-size:15px;font-weight:500;display:flex;align-items:center;gap:10px}
.top-contact svg{width:13px;height:13px;fill:var(--red)}
.main-nav{position:absolute;right:111px;top:66px;display:flex;gap:26px;color:var(--white);font-size:14px;font-weight:700}

/* hero */
.hero{position:absolute;left:0;top:111px;width:1200px;height:600px;background:linear-gradient(90deg,#b8aa98 0%,#8a7155 45%,#5e4330 75%,#3c2a1e 100%)}
.welcome-box{position:absolute;left:111px;top:186px;width:489px;height:227px;background:rgba(255,255,255,.82);text-align:center}
.welcome-box h1{font-size:44px;margin-top:22px;color:var(--ink)}
.welcome-box p{font-size:19px;font-weight:500;margin-top:6px}

/* about */
.about-frame{position:absolute;left:111px;top:795px;width:456px;height:342px;border:6px solid var(--red);border-right:none;border-bottom:none}
.about-frame::after{content:"";position:absolute;left:-6px;bottom:0;width:6px;height:0}
.about-photo{position:absolute;left:124px;top:809px;width:462px;height:347px;background:var(--white);box-shadow:0 2px 10px rgba(0,0,0,.18);padding:10px}
.about-photo div{width:100%;height:100%;background:linear-gradient(135deg,#7a6a58,#a58a6c 50%,#4a5672)}
.about-text{position:absolute;left:648px;top:800px;width:441px}
.about-text h2{font-size:40px}
.about-text p{font-size:15.5px;line-height:26px;color:var(--muted);text-align:justify;margin-top:16px}

/* team */
.team{position:absolute;left:0;top:1253px;width:1200px;height:475px;background:var(--light)}
.section-title{position:absolute;left:0;width:1200px;text-align:center;font-size:48px}
.member{position:absolute;top:145px;width:232px;height:236px}
.member .photo{width:232px;height:236px}
.member .tag{position:absolute;left:18px;top:195px;width:196px;height:79px;background:var(--white);box-shadow:0 2px 8px rgba(0,0,0,.12);text-align:center;padding-top:14px}
.member .tag h3{font-size:20px;font-weight:600;color:var(--red)}
.member .tag p{font-size:15px;margin-top:4px}
.member .tag.active{background:var(--red)}
.member .tag.active h3,.member .tag.active p{color:var(--white)}

/* contact */
.map{position:absolute;left:470px;top:1904px;width:619px;height:429px;background:var(--white);box-shadow:0 2px 10px rgba(0,0,0,.15);padding:7px}
.map div{width:100%;height:100%;background:linear-gradient(135deg,#9fbf8e,#ddd6c6 40%,#e2dccd 70%,#a9c498)}
.contact-form{position:absolute;left:111px;top:1947px;width:411px;height:343px;background:var(--white);box-shadow:0 2px 12px rgba(0,0,0,.14);padding:34px 34px}
.field{height:48px;background:var(--field);border-radius:8px;margin-bottom:13px;display:flex;align-items:center;padding-left:18px;gap:8px;font-size:15px;color:#555}
.field svg{width:14px;height:14px;fill:none;stroke:#666;stroke-width:2}
.field.tall{height:88px;align-items:flex-start;padding-top:16px}
.contact-form .btn{left:34px;top:257px;width:343px;height:52px;font-size:16px}

/* hours */
.hours{position:absolute;left:0;top:2429px;width:1200px;height:471px;background:linear-gradient(90deg,#6d5642 0%,#8d6f52 35%,#a39786 60%,#c2b8a8 100%)}
.hours-panel{position:absolute;left:789px;top:41px;width:300px;height:430px;background:rgba(255,255,255,.88);text-align:center;padding-top:20px}
.hours-panel h2{font-size:37px}
.hours-panel h4{font-size:18px;font-weight:600;margin-top:16px}
.hours-panel p{font-size:15.5px;color:var(--muted);margin-top:4px}
.hours-panel hr{border:none;height:4px;background:var(--dark);width:240px;margin:28px auto 18px}
.hours-panel .phone{font-size:26px;color:var(--red);font-weight:500}

/* events */
.event{position:absolute;top:3064px;width:310px;height:381px;background:var(--white);box-shadow:0 2px 10px rgba(0,0,0,.15);padding:7px}
.event .photo{width:296px;height:211px;position:relative}
.event .date{position:absolute;left:8px;top:192px;background:var(--red);color:var(--white);font-size:13px;font-weight:700;padding:8px 20px}
.event h3{font-size:20px;font-weight:600;color:var(--red);margin:40px 0 0 4px}
.event p{font-size:14px;line-height:23px;color:var(--muted);margin:14px 0 0 5px}

/* footer */
.site-footer{position:absolute;left:0;top:3621px;width:1200px;height:333px;background:var(--dark);color:var(--white);text-align:center}
.footer-brand{font-size:44px;font-weight:700;margin-top:50px}
.footer-nav{display:flex;justify-content:center;gap:30px;font-size:18px;font-weight:600;margin-top:26px}
.footer-contact{display:flex;justify-content:center;align-items:center;gap:12px;font-size:18px;font-weight:500;margin-top:24px}
.footer-contact svg{width:15px;height:15px;fill:var(--red)}
.social{display:flex;justify-content:center;gap:10px;margin-top:30px}
.social span{width:31px;height:31px;background:#444;border-radius:3px;display:block}
.social span.on{background:var(--red)}
.footer-rule{position:absolute;left:111px;top:278px;width:978px;height:1px;background:#444}
.copyright{position:absolute;left:0;top:299px;width:1200px;font-size:13px}
</style>
</head>
<body>

<header class="site-header">
  <div class="brand-panel"><span class="brand-name">The Makerloft Barn</span></div>
  <div class="top-contact">
    <svg viewBox="0 0 24 24"><path d="M6.6 10.8a15 15 0 0 0 6.6 6.6l2.2-2.2a1 1 0 0 1 1-.25 11.4 11.4 0 0 0 3.6.6 1 1 0 0 1 1 1V20a1 1 0 0 1-1 1A17 17 0 0 1 3 4a1 1 0 0 1 1-1h3.5a1 1 0 0 1 1 1c0 1.25.2 2.45.6 3.6a1 1 0 0 1-.25 1z"/></svg>
    <span>555-014-2780</span><span>&nbsp;|&nbsp;</span>
    <svg viewBox="0 0 24 24"><path d="M12 2a7 7 0 0 0-7 7c0 5 7 13 7 13s7-8 7-13a7 7 0 0 0-7-7zm0 9.5A2.5 2.5 0 1 1 12 6.5a2.5 2.5 0 0 1 0 5z"/></svg>
    <span>Lorum Ipsum Dol, United States</span>
  </div>
  <nav class="main-nav"><span>HOME</span><span>STUDIO ACTIVITIES</span><span>STUDIO EVENTS</span><span>RESOURCES</span><span>ONLINE SHOP</span></nav>
</header>

<section class="hero" role="img" aria-label="Smiling craftswoman in an apron holding a tablet in a pottery studio">
  <div class="welcome-box">
    <h1 class="script">Welcome To <span class="accent">Makerloft</span></h1>
    <p>Lorem ipsum dolor sit amet consea</p>
    <span class="btn" style="left:165px;top:140px;width:158px;height:50px">Get Started</span>
  </div>
</section>

<section class="about">
  <div class="about-frame"></div>
  <div class="abs" style="left:111px;top:795px;width:6px;height:342px;background:var(--red)"></div>
  <div class="about-photo"><div role="img" aria-label="Woman with glasses standing with arms crossed in a workshop"></div></div>
  <div class="about-text">
    <h2 class="script">About <span class="accent">Us</span></h2>
    <p>Lorem ipsum dolor sit amet, consectetur adipiscing elit, sed do eiusmod tempor incididunt ut labore et dolore magna aliqua. Ut enim ad minim veniam, quis nostrud exercitation ullamco laboris nisia.</p>
    <p>Tempor incididunt ut labore et dolore magna aliqua. Ut enim ad minim veniam, quis nostrud exercitation ullamco laboris nisia.</p>
    <span class="btn" style="left:0;top:300px;width:158px;height:50px">Learn More</span>
  </div>
</section>

<section class="team">
  <h2 class="section-title script" style="top:40px"><span class="accent">Meet</span> The Team</h2>
  <div class="member" style="left:111px"><div class="photo" role="img" aria-label="Smiling craftsman in a plaid shirt and apron" style="background:linear-gradient(160deg,#8b6a4f,#5a4636)"></div><div class="tag"><h3>Alex Rowan</h3><p>Lorem ipsum dola</p></div></div>
  <div class="member" style="left:360px"><div class="photo" role="img" aria-label="Potter with arms crossed in front of ceramic shelves" style="background:linear-gradient(160deg,#c9a98e,#8fa6b8)"></div><div class="tag"><h3>Alex Rowan</h3><p>Lorem ipsum dola</p></div></div>
  <div class="member" style="left:609px"><div class="photo" role="img" aria-label="Craftsman in denim at a brick-walled workbench" style="background:linear-gradient(160deg,#b46d55,#4f5f78)"></div><div class="tag active"><h3>Alex Rowan</h3><p>Lorem ipsum dola</p></div></div>
  <div class="member" style="left:857px"><div class="photo" role="img" aria-label="Woman in a yellow sweater and beanie working with wood" style="background:linear-gradient(160deg,#6e5a48,#d9a43a)"></div><div class="tag"><h3>Alex Rowan</h3><p>Lorem ipsum dola</p></div></div>
</section>

<section class="contact">
  <h2 class="section-title script" style="top:1805px">Contact <span class="accent">Us</span></h2>
  <div class="map"><div role="img" aria-label="Regional road map with the studio location marked"></div></div>
  <form class="contact-form">
    <div class="field"><svg viewBox="0 0 24 24"><circle cx="12" cy="8" r="4"/><path d="M4 21c0-4 4-6 8-6s8 2 8 6"/></svg>Name</div>
    <div class="field"><svg viewBox="0 0 24 24"><rect x="3" y="5" width="18" height="14" rx="2"/><path d="M3 7l9 6 9-6"/></svg>Your Email</div>
    <div class="field tall"><svg viewBox="0 0 24 24"><path d="M4 5h16v11H9l-5 4z"/></svg>How Can we hel you?</div>
    <span class="btn">Submit
      <svg width="16" height="16" viewBox="0 0 24 24" fill="none" stroke="#fff" stroke-width="2"><path d="M22 2L11 13M22 2l-7 20-4-9-9-4z"/></svg></span>
  </form>
</section>

<section class="hours" role="img" aria-label="Potter glazing a ceramic cup at a studio table">
  <div class="hours-panel">
    <h2 class="script">Operating <span class="accent">Hours</span></h2>
    <h4>MONDAY - FRIDAY</h4><p>9.00 AM - 6.00 PM</p>
    <h4>SATURDAY</h4><p>9.00 AM - 5.00 PM</p>
    <h4>SUNDAY</h4><p>CLOSED</p>
    <hr>
    <div class="phone">555-014-2780</div>
  </div>
</section>

<section class="events">
  <h2 class="section-title script" style="top:2978px;font-size:40px">Studio <span class="accent">Events</span></h2>
  <article class="event" style="left:111px"><div class="photo" role="img" aria-label="Hands cutting leather with a knife" style="background:linear-gradient(135deg,#3a2a20,#a5673a)"><span class="date">14 SEP 2021</span></div><h3>Lorem ipsum dolor sitama</h3><p>Sed ut perspiciatis unde omnis iste na tus error sit voluptatem accus ant ium doloremque lauadantiuma...</p></article>
  <article class="event" style="left:445px"><div class="photo" role="img" aria-label="Artist painting with ink and brushes" style="background:linear-gradient(135deg,#5d5a55,#d8cfc2)"><span class="date">14 SEP 2021</span></div><h3>Lorem ipsum dolor sitama</h3><p>Sed ut perspiciatis unde omnis iste na tus error sit voluptatem accus ant ium doloremque lauadantiuma...</p></article>
  <article class="event" style="left:779px"><div class="photo" role="img" aria-label="Pressed autumn leaves arranged on paper" style="background:linear-gradient(135deg,#b0522c,#e6dccb 60%,#d9823a)"><span class="date">14 SEP 2021</span></div><h3>Lorem ipsum dolor sitama</h3><p>Sed ut perspiciatis unde omnis iste na tus error sit voluptatem accus ant ium doloremque lauadantiuma...</p></article>
  <span class="btn" style="left:521px;top:3493px;width:159px;height:51px">Book Now</span>
</section>

<footer class="site-footer">
  <div class="footer-brand">The Makerloft Barn</div>
  <nav class="footer-nav"><span>HOME</span><span>STUDIO ACTIVITIES</span><span>STUDIO EVENTS</span><span>RESOURCES</span><span>ONLINE SHOP</span></nav>
  <div class="footer-contact">
    <svg viewBox="0 0 24 24"><path d="M6.6 10.8a15 15 0 0 0 6.6 6.6l2.2-2.2a1 1 0 0 1 1-.25 11.4 11.4 0 0 0 3.6.6 1 1 0 0 1 1 1V20a1 1 0 0 1-1 1A17 17 0 0 1 3 4a1 1 0 0 1 1-1h3.5a1 1 0 0 1 1 1c0 1.25.2 2.45.6 3.6a1 1 0 0 1-.25 1z"/></svg>
    <span>555-014-2780</span><span>&nbsp;|&nbsp;</span>
    <svg viewBox="0 0 24 24"><path d="M12 2a7 7 0 0 0-7 7c0 5 7 13 7 13s7-8 7-13a7 7 0 0 0-7-7zm0 9.5A2.5 2.5 0 1 1 12 6.5a2.5 2.5 0 0 1 0 5z"/></svg>
    <span>Lorum Ipsum Dol, United States</span>
  </div>
  <div class="social"><span class="on"></span><span></span><span></span><span></span></div>
  <div class="footer-rule"></div>
  <div class="copyright">© 2021 The Makerloft Barn. All Rights Reserved</div>
</footer>

</body>
</html>
```